I need a brochure that I can give to prospective clients during meetings and shows. My company website is www.brightlanternweb.com

There is information to help with the creation of the brochure. Additionally, I will be attaching the new company logo. The website is being fixed behind the scenes to incorporate the new logo and color schemes. Please allow the colors in the brochure to the logo and not the current website.

Thanks!

```html
<!DOCTYPE html>
<html lang="en">
<head>
<meta charset="utf-8">
<title>Brightlantern Brochure</title>
<link rel="stylesheet" href="https://fonts.googleapis.com/css2?family=Open+Sans:ital,wght@0,400;0,600;0,700;1,400;1,600&family=Roboto+Condensed:wght@400;700&display=swap">
<style>
:root{
  --bg:#e9e5df;
  --green:#1e8b30;
  --green-dark:#2c6a22;
  --lime:#9acb3b;
  --lime-soft:#b5d96a;
  --ink-green:#2d7a1f;
  --text-dark:#3a5a1c;
  --grey-text:#6d6d6d;
  --paper:#f4f4f2;
  --white:#ffffff;
  --gold:#d6e84a;
}
*{box-sizing:border-box;margin:0;padding:0}
html,body{width:1200px;height:960px;overflow:hidden;background:var(--bg);font-family:"Open Sans",sans-serif}
.canvas{position:relative;width:1200px;height:960px}
.panel-label{position:absolute;top:900px;font-size:15px;letter-spacing:4px;color:#7a746c;text-align:center;width:300px}

/* front cover */
.cover{position:absolute;top:210px;width:300px;height:660px;background:var(--green);box-shadow:4px 6px 0 #17702a,8px 12px 14px rgba(0,0,0,.25)}
.cover.front{left:40px}
.cover.back{left:860px}
.brand{display:flex;flex-direction:column;align-items:center}
.brand-row{display:flex;align-items:center;gap:8px}
.brand-mark{width:30px;height:30px;border-radius:50%;background:var(--lime)}
.brand-name{font-weight:600;color:var(--lime);letter-spacing:3px}
.front .brand{position:absolute;top:340px;left:0;right:0}
.front .brand-name{font-size:22px}
.front .site{margin-top:8px;font-size:10px;font-weight:600;color:var(--gold);letter-spacing:.5px}

/* back cover */
.back .brand{position:absolute;top:300px;left:0;right:0}
.back .brand-mark{width:20px;height:20px}
.back .brand-name{font-size:12px;letter-spacing:2px}
.contact{position:absolute;top:350px;left:0;right:0;text-align:center;color:var(--gold)}
.contact .lead{font-family:"Roboto Condensed",sans-serif;font-weight:700;font-size:17px;letter-spacing:2px;color:#f1f4c8}
.contact .call{margin-top:10px;font-size:10px}
.contact .call b{font-size:19px;font-weight:400;margin-left:4px}
.contact .visit{font-size:12px;font-weight:700}
.contact .addr,.contact .site{font-size:10px;font-weight:600;line-height:1.35}
.social{display:flex;justify-content:center;gap:12px;margin-top:8px}
.social span{width:16px;height:16px;border-radius:50%;background:var(--lime)}

/* inside spread */
.spread{position:absolute;left:370px;top:40px;width:460px;height:700px;display:flex;box-shadow:6px 10px 16px rgba(0,0,0,.25)}
.page{position:relative;width:230px;height:100%}
.page.left{background:var(--lime)}
.page.right{background:var(--paper)}
.feature-card{position:absolute;left:10px;top:10px;width:210px;height:230px;background:var(--white);border-radius:6px;box-shadow:0 2px 4px rgba(0,0,0,.15)}
.feature-art{position:absolute;left:60px;top:22px;width:90px;height:110px;border-radius:6px;background:linear-gradient(160deg,#d8a862,#b57b3a)}
.feature-title{position:absolute;left:0;right:0;top:178px;text-align:center;font-size:16px;font-weight:600;color:var(--green-dark);letter-spacing:.5px}
.feature-notch{position:absolute;left:98px;bottom:-7px;width:14px;height:14px;background:var(--white);transform:rotate(45deg)}
.quote{position:absolute;left:18px;right:14px;top:256px;font-style:italic;font-weight:600;font-size:12.5px;line-height:1.3;color:var(--text-dark)}
.left-copy{position:absolute;left:18px;right:14px;top:318px;font-size:8.6px;line-height:1.3;color:var(--text-dark)}
.left-copy p+p{margin-top:8px}
.url-band{position:absolute;left:0;right:0;bottom:0;height:76px;background:var(--green-dark);color:#b8d98a;font-size:9.5px;letter-spacing:2px;padding:30px 0 0 14px}

.intro{position:absolute;left:14px;right:12px;top:50px;font-size:12.5px;line-height:1.35;color:var(--grey-text);text-align:right}
.intro strong{color:var(--green-dark);font-weight:700}
.info-card{position:absolute;left:12px;right:10px;top:170px;height:420px;background:var(--white);border-radius:6px;box-shadow:0 1px 4px rgba(0,0,0,.18);padding:16px 12px}
.info-card h2{font-size:14px;font-weight:400;color:#3a3a3a;line-height:1.25}
.info-card p{font-size:7.8px;line-height:1.3;color:#4a4a4a;margin-top:14px}
.services{position:absolute;left:12px;right:8px;bottom:20px;display:grid;grid-template-columns:1fr 1fr;row-gap:10px;font-family:"Roboto Condensed",sans-serif;font-size:11.5px;color:var(--green-dark)}
.services li{list-style:none;padding:4px 0}
.services li:nth-child(even){border-left:1px solid #c6c6c6;padding-left:8px;text-align:center}
</style>
</head>
<body>
<div class="canvas">

  <section class="cover front">
    <div class="brand">
      <div class="brand-row"><span class="brand-mark"></span><span class="brand-name">BRIGHTLANTERN</span></div>
      <div class="site">www.brightlanternweb.com</div>
    </div>
  </section>
  <div class="panel-label" style="left:40px">FRONT</div>

  <section class="spread">
    <div class="page left">
      <div class="feature-card">
        <div class="feature-art" role="img" aria-label="Illustration of a cardboard box filled with social media symbols"></div>
        <h1 class="feature-title">DIGITAL MEDIA MARKETING</h1>
        <div class="feature-notch"></div>
      </div>
      <p class="quote">“Strategies focused on increasing the Reach and Visibility of your Business”</p>
      <div class="left-copy">
        <p>There are many different ways a company can implement Digital Marketing and Social Media into their business strategy. It takes knowledge and experience in both of these areas to create a truly effective approach that will maximize available resources and grow a strong digital presence.</p>
        <p>At Brightlantern, we can help your business to define and implement the best Digital Marketing and Social Media strategy in order to achieve your company's organizational goals.</p>
        <p>Contact Brightlantern to schedule a complimentary consultation in order to learn more about how a Digital Marketing and Social Media strategy will benefit your company.</p>
      </div>
      <div class="url-band">www.brightlanternweb.com</div>
    </div>
    <div class="page right">
      <p class="intro">You want to connect with more clients.<br>We have the <strong>SEARCH ENGINE OPTIMIZATION</strong> and <strong>DIGITAL MARKETING SERVICES</strong> you need to make that happen.</p>
      <div class="info-card">
        <h2>Why Digital Marketing and Search Engine Optimization?</h2>
        <p>In today's business environment, it's really hard to get noticed. There's a lot of competition out there. That's why when it comes to getting an edge, businesses need to be doing everything they can to succeed. Search Engine Optimization is no longer a question of should we do it, but more like how much should we do. Digital Marketing and SEO Services can help to cut through all the noise and deliver powerful content to target audiences. Brightlantern provides Digital Marketing and SEO Services and SEO Marketing to help businesses grow by improving organic search ranks and delivering their message to the right audience.</p>
        <p>Call Brightlantern to set up a complimentary Digital Marketing and SEO Services consultation, so you can learn how Digital Marketing and SEO Services will directly impact your visibility to potential customers. We will provide updates using SEO tools to keep you informed. Have your company ranking higher in search engine results using successful Digital Marketing and SEO Services, ultimately promoting higher client traffic to your company's website. That increased traffic will translate into a higher number of converted sales and will directly lead to increased earnings for your business. Brightlantern is an experienced SEO Company that can help your business reach its organizational goals.</p>
      </div>
      <ul class="services">
        <li>Search Engine Optimization</li>
        <li>SEO Training</li>
        <li>SEO Consulting Services</li>
        <li>Digital Marketing Services</li>
      </ul>
    </div>
  </section>
  <div class="panel-label" style="left:450px">FLIP-OVER</div>

  <section class="cover back">
    <div class="brand">
      <div class="brand-row"><span class="brand-mark"></span><span class="brand-name">BRIGHTLANTERN</span></div>
    </div>
    <div class="contact">
      <div class="lead">TO CONNECT WITH US...</div>
      <div class="call">Call Us:<b>808 555 0142</b></div>
      <div class="visit">or Visit Us:</div>
      <div class="addr">418 Kealoha Lane, Honolulu, HI 96814</div>
      <div class="site">www.brightlanternweb.com</div>
      <div class="social"><span></span><span></span><span></span></div>
    </div>
  </section>
  <div class="panel-label" style="left:860px">BACK</div>

</div>
</body>
</html>
```